Skin cancer clinic services trifold brochure

Need trifold brochure listing skin cancer services our clinic provides, staff information, location and brief about skin cancer with colours similar to our web site www.Lumorava.clinic. I will provide more information regarding services and staff but want this colourful and standout as it will be given to other referring doctors or patients

Target Market(s)

Age 40 to 80 years

Industry/Entity Type

Medical

Font styles to use
Serif

Colors

Designer to choose colors to be used in the design.

Requirements
Must have
• Logo, services, contact info, beach or sun look and colours similar to web site or logo

```html
<!DOCTYPE html>
<html lang="en">
<head>
<meta charset="utf-8">
<title>Lumorava Skin Cancer Clinic – Treatment &amp; Services</title>
<link rel="stylesheet" href="https://fonts.googleapis.com/css2?family=Carlito:wght@400;700&family=Jost:wght@600;700&display=swap">
<style>
  :root {
    --orange: #e8822a;
    --sky: #35a0e0;
    --heading-blue: #2f9ade;
    --grey: #b6b6b6;
    --plum: #93205f;
    --ink: #111111;
    --paper: #ffffff;
    --sea-light: #9fd3ea;
    --sea-deep: #2f86b8;
  }
  * { margin: 0; padding: 0; box-sizing: border-box; }
  html, body { width: 1200px; height: 927px; overflow: hidden; background: var(--paper); }
  .brochure {
    position: relative; width: 1200px; height: 927px; overflow: hidden;
    background: var(--paper); font-family: "Carlito", "Calibri", sans-serif; color: var(--plum);
  }
  .backdrop { position: absolute; inset: 0; width: 1200px; height: 927px; }
  .block { position: absolute; }
  .section-title {
    font-family: "Jost", sans-serif; font-weight: 700; color: var(--heading-blue);
    font-size: 26.5px; letter-spacing: 0.3px; line-height: 1; white-space: nowrap;
  }
  .sub-title {
    font-family: "Jost", sans-serif; font-weight: 700; color: var(--ink);
    font-size: 27px; line-height: 1; white-space: nowrap;
  }
  .copy { font-size: 21px; line-height: 25.3px; }
  .service-list { list-style: none; font-size: 21px; line-height: 39.5px; white-space: nowrap; }
  .treatment-list { list-style: none; font-size: 21px; line-height: 25.3px; white-space: nowrap; }
  .procedure-list {
    list-style: none; font-family: "Jost", sans-serif; font-weight: 700;
    color: var(--ink); font-size: 27px; line-height: 33px;
  }
  .conditions { text-align: center; font-size: 21px; line-height: 25.3px; white-space: nowrap; }
  .callout { font-weight: 700; }
  .brand {
    position: absolute; left: 962px; top: 840px; display: flex; align-items: center; gap: 10px;
  }
  .brand-dot { width: 24px; height: 24px; border-radius: 50%; background: var(--orange); }
  .brand-name {
    font-family: "Carlito", sans-serif; font-weight: 700; font-size: 32px;
    color: var(--ink); letter-spacing: 1px; line-height: 1; white-space: nowrap;
  }
</style>
</head>
<body>
<main class="brochure">
  <svg class="backdrop" viewBox="0 0 1200 927">
    <defs>
      <linearGradient id="sea" x1="0" y1="0" x2="1" y2="1">
        <stop offset="0" stop-color="#9fd3ea"/>
        <stop offset="1" stop-color="#2f86b8"/>
      </linearGradient>
    </defs>
    <path role="img" aria-label="Photo of a person splashing through shallow sea water at the beach"
          d="M0,0 H735 C450,75 200,150 0,262 Z" fill="url(#sea)"/>
    <path class="band-grey" d="M0,286 C120,220 300,200 500,185 C560,180 590,165 604,151 C560,178 500,184 420,192 C250,207 100,222 0,292 Z" fill="var(--grey)"/>
    <path class="band-orange" d="M0,262 C150,170 450,70 735,0 L852,0 C760,70 600,110 450,135 C250,170 100,200 0,270 Z" fill="var(--orange)"/>
    <path class="band-blue" d="M148,190 C350,140 600,120 794,41 C700,120 550,140 380,162 C280,174 200,184 148,190 Z" fill="var(--sky)"/>
    <path class="foot-grey" d="M0,808 C150,860 300,880 500,880 C800,880 1050,780 1200,680 V927 H0 Z" fill="var(--grey)"/>
    <path class="foot-blue" d="M143,862 C400,880 700,870 900,800 C1000,765 1100,710 1200,654 V672 C1100,730 1000,790 880,830 C700,890 400,895 143,862 Z" fill="var(--sky)"/>
  </svg>

  <!-- Left panel -->
  <h2 class="block section-title" style="left:35px; top:283px;">TREATMENT &amp; SERVICES</h2>
  <h3 class="block sub-title" style="left:36px; top:335px;">Our Specialised Services</h3>
  <ul class="block service-list" style="left:34px; top:368px;">
    <li>- Skin cancer detection</li>
    <li>- Mole assessment</li>
    <li>- Digital monitoring of moles</li>
    <li>- Medical treatment of skin cancer</li>
    <li>- Surgical treatment of skin cancer</li>
    <li>- General dermatologic surgery</li>
    <li>- Same day ‘slow MOHs’ procedures</li>
  </ul>
  <h3 class="block sub-title" style="left:35px; top:682px;">Treatments</h3>
  <ul class="block procedure-list" style="left:34px; top:719px;">
    <li>EXCISION</li>
    <li>CURETTAGE</li>
    <li>CRYOSURGERY</li>
  </ul>

  <!-- Middle panel -->
  <h2 class="block section-title" style="left:454px; top:214px;">COSMETICS SERVICES</h2>
  <p class="block copy" style="left:423px; top:250px; width:345px;">Our mission is to help people with a range of conditions, with our advanced technology &amp; well trained staff.</p>
  <p class="block conditions" style="left:429px; top:336px; width:344px;">
    Veins | Pigmentation<br>Skin Rejuvenation | Rosacea<br>Wrinkles | Acne Scarring<br>Poor Skin Texture | Large Pores<br>Unwanted Scars | Skin Blemishes<br>Sun Damaged Skin | Hair Removal
  </p>
  <h3 class="block sub-title" style="left:423px; top:502px;">Treatments</h3>
  <ul class="block treatment-list" style="left:423px; top:539px;">
    <li>- YAG LASER</li>
    <li>- LUMIRAY IPL</li>
    <li>- LASER RENOVA</li>
    <li>- OPALINE / OPALINE FRACTIONAL</li>
    <li>- FLUX WAVE</li>
  </ul>
  <h3 class="block sub-title" style="left:423px; top:692px;">Other Services</h3>
  <p class="block copy" style="left:423px; top:733px; width:340px;"><span class="callout">ANTI -WRINKLE INJECTIONS AND DERMAL FILLERS</span> - a substance found naturally in our skin. They can be used for:</p>

  <!-- Right panel -->
  <ul class="block treatment-list" style="left:819px; top:33px;">
    <li>- Thin lips or lip augmentation</li>
    <li>- Under eye rejuvenation or tear troughs</li>
    <li>- Nasolabial lines and cheek augmentation</li>
    <li>- Non-surgical nose correction</li>
    <li>- Brow lift</li>
    <li>- Forehead lines</li>
    <li>- Temple rejuvenation</li>
    <li>- Non-surgical jaw correction</li>
  </ul>
  <p class="block copy callout" style="left:819px; top:262px; width:370px;">WE RECOMMEND ANTI-WRINKLE<br>INJECTIONS FOR:</p>
  <ul class="block treatment-list" style="left:819px; top:339px;">
    <li>Glabellar (between the brows)</li>
    <li>Crow’s feet (eyes)</li>
    <li>Upper lip lines (smoker’s lines)</li>
    <li>Forehead lines</li>
    <li>Bunny lines (nose lines)</li>
    <li>Chin lines</li>
    <li>Downturned mouth</li>
    <li>Platysmal Band (neck)</li>
  </ul>
  <p class="block copy" style="left:819px; top:568px; width:345px;"><span class="callout">TENSIFORM -</span> is the world’s number one system for skin tightening. It is a multifunctional ultrasound device, offering&nbsp; face and neck tightening, as well as body contouring in one system.</p>

  <div class="brand">
    <span class="brand-dot"></span>
    <span class="brand-name">LUMORAVA</span>
  </div>
</main>
</body>
</html>
```